QuadLantern--Help Us look fresh and new to companies, college students and college career centers!

We just designed a new logo and would like to freshen-up and make our business cards a bit more modern. Not crazy-modern like Velmont, but modern like metro-style and fresh like fruit. We use three logos with a combination of two colors each, and three colors total. We are looking for a single format to apply to three different cards/color schemes (green/blue to give out to companies, orange/green for students, and orange/blue for university career centers). Thanks everyone--looking forward to seeing your designs!!

Target Market(s)

Three styles: companies, college students/grads, college career centers

Industry/Entity Type

College

Contact Information for Business Card

Address: 5718 Harlow Street, Suite 412, Seattle, WA 98109. Need a spot for email address, web address (www.quadlantern.example), and phone numbers (main, direct, mobile). Don't open that website unless you want to lose your lunch--it is waaaay old and outdated. See this link instead, http://preview.mossgrovedev.example/QuadLantern/HiringTools, for our new website design in progress.

Font styles to use
Sans Serif

Requirements
Must have
• Please use the logos supplied. Would like text to be grey but printable, like a "light" type style that is metro-type with sans-serif. NOT black text. Modern. For inspiration, here's a link to our work-in-progress website we are planning to launch soon: http://preview.mossgrovedev.example/QuadLantern/HiringTools
Nice to have
• Would like to see something unique and different in a "metro" style. Clean and not cluttered.
Should not have
• No odd-sized cards

```html
<!DOCTYPE html>
<html lang="en">
<head>
<meta charset="utf-8">
<title>QuadLantern Business Card</title>
<link href="https://fonts.googleapis.com/css2?family=Exo+2:wght@300;400;500&display=swap" rel="stylesheet">
<style>
  :root {
    --bg: #9a9a9a;
    --green: #7cc242;
    --blue: #1a7fc6;
    --card-white: #f4f4f4;
    --text-grey: #3c3c3c;
    --title-grey: #555555;
  }
  * { margin: 0; padding: 0; box-sizing: border-box; }
  html, body { width: 1200px; height: 894px; overflow: hidden; }
  body {
    background: var(--bg);
    font-family: "Exo 2", sans-serif;
    position: relative;
  }
  .card {
    position: absolute;
    width: 520px;
    height: 297px;
    top: 298px;
    overflow: hidden;
    box-shadow: 0 6px 18px rgba(0,0,0,0.25);
  }
  .card-back { left: 60px; background: linear-gradient(135deg, #e9e9e9, var(--card-white) 45%, #e6e6e6); }
  .card-front { left: 620px; background: var(--green); }

  /* back */
  .name { position: absolute; left: 30px; top: 26px; font-size: 22px; font-weight: 400; color: var(--green); }
  .job-title { position: absolute; left: 30px; top: 55px; font-size: 9px; letter-spacing: 1px; color: var(--title-grey); }
  .contact-list { position: absolute; left: 30px; top: 80px; }
  .contact-row { display: flex; height: 20px; align-items: center; font-size: 14px; }
  .contact-label { width: 78px; color: var(--green); }
  .contact-value { color: var(--text-grey); letter-spacing: 0.5px; }
  .address { position: absolute; left: 30px; top: 182px; display: flex; align-items: center; gap: 10px; font-size: 14px; color: var(--text-grey); letter-spacing: 0.5px; }
  .rule { position: absolute; height: 2px; background: var(--blue); }
  .rule-contact { left: 0; top: 168px; width: 310px; }
  .rule-address { left: 20px; top: 210px; width: 500px; }
  .rule-bottom { left: 20px; top: 270px; width: 500px; }
  .accent-pill { position: absolute; left: 405px; top: 112px; width: 140px; height: 58px; border-radius: 29px; background: var(--blue); }
  .faint-mark { position: absolute; left: 330px; top: 160px; width: 60px; height: 60px; border-radius: 50%; background: rgba(26,127,198,0.08); }

  /* front */
  .logo-band { position: absolute; right: 0; top: 168px; width: 250px; height: 64px; background: #ffffff; border-radius: 32px 0 0 32px; display: flex; align-items: center; padding-left: 22px; gap: 10px; }
  .logo-dot { width: 26px; height: 26px; border-radius: 50%; background: var(--green); }
  .logo-name { font-size: 27px; font-weight: 500; color: var(--blue); }
  .front-strip { position: absolute; right: 0; top: 232px; width: 250px; height: 14px; background: #ffffff; }
</style>
</head>
<body>
  <section class="card card-back">
    <div class="faint-mark"></div>
    <div class="accent-pill"></div>
    <h1 class="name">Daniel Okafor</h1>
    <p class="job-title">GENERAL MANAGER</p>
    <div class="contact-list">
      <div class="contact-row"><span class="contact-label">Phone:</span><span class="contact-value">012 555 0147</span></div>
      <div class="contact-row"><span class="contact-label">Fax:</span><span class="contact-value">012 555 0148</span></div>
      <div class="contact-row"><span class="contact-label">Email:</span><span class="contact-value">hello@quadlantern.example</span></div>
      <div class="contact-row"><span class="contact-label">website:</span><span class="contact-value">www.quadlantern.example</span></div>
    </div>
    <div class="rule rule-contact"></div>
    <div class="address">
      <svg width="14" height="18" viewBox="0 0 14 18" aria-hidden="true">
        <path d="M7 0C3.1 0 0 3.1 0 7c0 5 7 11 7 11s7-6 7-11c0-3.9-3.1-7-7-7z" fill="#7cc242"/>
        <circle cx="7" cy="7" r="2.6" fill="#ffffff"/>
      </svg>
      <span>5718 Harlow Street, Suite 412, Seattle</span>
    </div>
    <div class="rule rule-address"></div>
    <div class="rule rule-bottom"></div>
  </section>

  <section class="card card-front">
    <div class="logo-band">
      <span class="logo-dot"></span>
      <span class="logo-name">QuadLantern</span>
    </div>
    <div class="front-strip"></div>
  </section>
</body>
</html>
```